Business Card & Email Signature Design || Upmarket + Luxury

Riverlume Honey, a New Zealand Manuka Honey company needs a Business Card & Email Signature design.

Our logo's are attached in Gold & Black versions, feel free to be creative with how you use the logo and it's patterns in your design.

Style:
- Looking for an Elegant, Luxurious, Upmarket feel.
- Black/Matte Black Card, Gold Foil, UV Embossing

Information to Add:

- Logo
- Company Name: Riverlume Honey
- Name: Mattias Brovell
- Title: Creative Director
- Phone: +64 2919 58 617
- Email: mattias@riverlumehoney.example
- Website: www.riverlumehoney.example

- Socials: ***For email Signature Only***
- Facebook: https://www.facebook.com/riverlumehoney/
- Instagram: https://www.instagram.com/riverlumehoney/

Target Market(s)

Asia/Europe Luxury, Upmarket

Contact Information for Business Card

- Logo
- Name: Mattias Brovell
- Phone: +64 2919 58 617

Font styles to use
Other font styles liked:
• Champagne & Limousines (Attached)

Requirements
Must have
• Business Card & Email Signature Design.

Looking for a Sleek, Luxury, Upmarket Design.

```html
<!DOCTYPE html>
<html lang="en">
<head>
<meta charset="utf-8">
<title>Riverlume Honey – Business Card &amp; Email Signature</title>
<link rel="stylesheet" href="https://fonts.googleapis.com/css2?family=Josefin+Sans:ital,wght@0,300;0,400;0,600;1,600&display=swap">
<style>
  :root {
    --board: #c9cacc;
    --label: #ffffff;
    --cream: #fbf6e3;
    --ink: #1d1d1d;
    --badge: #2a2a2a;
    --gold: #c9a55a;
    --gold-deep: #a8842f;
    --gold-text: #9d8552;
    --social-bar: #c9a86a;
    --social-label: #8b6a30;
    --icon-green: #6a9a1f;
    --icon-blue: #2f7fc0;
    --icon-plum: #6b3a68;
    --icon-amber: #d9a91a;
  }
  * { margin: 0; padding: 0; box-sizing: border-box; }
  html, body { width: 1200px; height: 1200px; overflow: hidden; }
  body {
    background: var(--board);
    font-family: "Josefin Sans", sans-serif;
    position: relative;
  }
  .version {
    position: absolute; top: 26px; right: 40px;
    color: var(--label); font-size: 16px; letter-spacing: 3px; font-weight: 600;
  }
  .section-label {
    position: absolute; left: 0; width: 1186px; text-align: center;
    color: var(--label); font-size: 16px; letter-spacing: 4px; font-weight: 600;
  }
  .section-label.cards { top: 106px; }
  .section-label.signature { top: 656px; }
  .piece {
    position: absolute; overflow: hidden;
    box-shadow: 0 2px 6px rgba(0,0,0,.3);
    background: var(--cream);
  }
  .piece svg { display: block; }
  .card-front { left: 32px; top: 176px; width: 560px; height: 318px; }
  .card-back { left: 605px; top: 176px; width: 562px; height: 318px; }
  .email-signature { left: 156px; top: 709px; width: 830px; height: 356px; }

  .person-given { font-weight: 300; fill: var(--gold-text); }
  .person-family { font-weight: 600; fill: var(--gold-text); }
  .job-title { font-style: italic; font-weight: 600; fill: var(--gold-deep); }
  .contact { font-weight: 300; fill: var(--gold-text); }
  .brand-badge { font-weight: 400; fill: var(--gold); letter-spacing: 2px; }
  .brand-name { font-weight: 400; fill: var(--gold); letter-spacing: 4px; }
  .social-label { font-weight: 400; fill: var(--social-label); }
  .social-handle { font-weight: 600; fill: #ffffff; }
  text { font-family: "Josefin Sans", sans-serif; }
</style>
</head>
<body>
  <div class="version">V1</div>
  <div class="section-label cards">BUSINESS CARD</div>

  <!-- Business card, front -->
  <div class="piece card-front">
    <svg width="560" height="318" viewBox="0 0 560 318">
      <rect width="560" height="318" fill="var(--cream)"/>
      <circle class="black-field" cx="48" cy="180" r="240" fill="var(--ink)" stroke="var(--gold)" stroke-width="2"/>
      <circle class="outer-ring" cx="110" cy="190" r="150" fill="none" stroke="var(--gold)" stroke-width="1.5"/>
      <path class="name-band" d="M560 72 H100 A90 90 0 0 0 100 252 H560 Z" fill="var(--cream)" stroke="var(--gold)" stroke-width="1.5"/>
      <circle class="brand-seal" cx="100" cy="160" r="76" fill="var(--badge)"/>
      <text class="brand-badge" x="100" y="156" font-size="15" text-anchor="middle">RIVERLUME</text>
      <text class="brand-badge" x="100" y="176" font-size="15" text-anchor="middle">HONEY</text>

      <text x="247" y="120" font-size="23"><tspan class="person-given">MATTIAS </tspan><tspan class="person-family">BROVELL</tspan></text>
      <text class="job-title" x="250" y="141" font-size="16">Creative Director</text>
      <line x1="250" y1="147" x2="392" y2="147" stroke="var(--gold)" stroke-width="1"/>
      <circle cx="394" cy="147" r="2.5" fill="var(--gold)"/>

      <g class="icon-phone" transform="translate(227 186)">
        <circle r="10" fill="var(--icon-green)"/>
        <path d="M-4 -5 l2 -1 2 3 -1.5 1.2 a7 7 0 0 0 3.3 3.3 l1.2 -1.5 3 2 -1 2 c-5 1 -10 -4 -9 -9z" fill="#fff"/>
      </g>
      <text class="contact" x="253" y="192" font-size="17">+64 2919 58 617</text>

      <g class="icon-mail" transform="translate(216 214)">
        <circle r="10" fill="var(--icon-blue)"/>
        <rect x="-5.5" y="-4" width="11" height="8" fill="none" stroke="#fff" stroke-width="1.3"/>
        <path d="M-5.5 -4 L0 1 L5.5 -4" fill="none" stroke="#fff" stroke-width="1.3"/>
      </g>
      <text class="contact" x="240" y="220" font-size="15">mattias@riverlumehoney.example</text>

      <g class="icon-web" transform="translate(302 296)">
        <circle r="9" fill="var(--icon-plum)"/>
        <circle r="4.5" fill="none" stroke="#fff" stroke-width="1.2"/>
        <line x1="-4.5" y1="0" x2="4.5" y2="0" stroke="#fff" stroke-width="1"/>
      </g>
      <text class="contact" x="316" y="301" font-size="16" font-weight="400">www.riverlumehoney.example</text>
    </svg>
  </div>

  <!-- Business card, back -->
  <div class="piece card-back">
    <svg width="562" height="318" viewBox="0 0 562 318">
      <rect width="562" height="318" fill="var(--cream)"/>
      <text class="brand-name" x="281" y="182" font-size="36" text-anchor="middle">RIVERLUME HONEY</text>
      <text class="brand-name" x="281" y="208" font-size="14" text-anchor="middle">CO.</text>
      <circle cx="283" cy="380" r="152" fill="var(--ink)" stroke="var(--gold)" stroke-width="2"/>
      <circle cx="283" cy="380" r="105" fill="none" stroke="var(--gold)" stroke-width="1.5"/>
    </svg>
  </div>

  <div class="section-label signature">EMAIL SIGNATURE</div>

  <!-- Email signature -->
  <div class="piece email-signature">
    <svg width="830" height="356" viewBox="0 0 830 356">
      <rect width="830" height="356" fill="var(--cream)"/>
      <circle class="black-field" cx="60" cy="200" r="326" fill="var(--ink)" stroke="var(--gold)" stroke-width="2"/>
      <circle class="outer-ring" cx="150" cy="205" r="160" fill="none" stroke="var(--gold)" stroke-width="1.5"/>
      <path class="name-band" d="M830 65 H156 A126 126 0 0 0 156 317 H830 Z" fill="var(--cream)" stroke="var(--gold)" stroke-width="1.5"/>
      <circle class="brand-seal" cx="150" cy="188" r="105" fill="var(--badge)"/>
      <text class="brand-badge" x="150" y="183" font-size="20" text-anchor="middle">RIVERLUME</text>
      <text class="brand-badge" x="150" y="209" font-size="20" text-anchor="middle">HONEY</text>

      <text x="306" y="111" font-size="31"><tspan class="person-given">MATTIAS </tspan><tspan class="person-family">BROVELL</tspan></text>
      <text class="job-title" x="314" y="139" font-size="22">Creative Director</text>
      <line x1="314" y1="147" x2="500" y2="147" stroke="var(--gold)" stroke-width="1"/>
      <circle cx="502" cy="147" r="3" fill="var(--gold)"/>

      <g class="icon-phone" transform="translate(298 199)">
        <circle r="13" fill="var(--icon-amber)" stroke="var(--gold)" stroke-width="1.5"/>
        <path d="M-5 -6 l2.5 -1.2 2.5 3.6 -2 1.5 a8 8 0 0 0 4 4 l1.5 -2 3.6 2.5 -1.2 2.5 c-6 1.2 -12 -4.8 -10.9 -10.9z" fill="#fff"/>
      </g>
      <text class="contact" x="326" y="209" font-size="27">+64 2919 58 617</text>

      <g class="icon-mail" transform="translate(289 236)">
        <circle r="13" fill="var(--icon-green)" stroke="var(--gold)" stroke-width="1.5"/>
        <rect x="-6.5" y="-4.5" width="13" height="9" fill="none" stroke="#fff" stroke-width="1.4"/>
        <path d="M-6.5 -4.5 L0 1 L6.5 -4.5" fill="none" stroke="#fff" stroke-width="1.4"/>
      </g>
      <text class="contact" x="318" y="246" font-size="25">mattias@riverlumehoney.example</text>

      <g class="icon-web" transform="translate(270 269)">
        <circle r="13" fill="var(--icon-plum)" stroke="var(--gold)" stroke-width="1.5"/>
        <circle r="5.5" fill="none" stroke="#fff" stroke-width="1.3"/>
        <line x1="-5.5" y1="0" x2="5.5" y2="0" stroke="#fff" stroke-width="1.1"/>
      </g>
      <text class="contact" x="305" y="278" font-size="24">www.riverlumehoney.example</text>

      <text class="social-label" x="822" y="260" font-size="19" text-anchor="end">SOCIAL MEDIA:</text>
      <path class="social-bar" d="M830 277 H616 A20 20 0 0 0 616 317 H830 Z" fill="var(--social-bar)"/>
      <circle cx="620" cy="297" r="12" fill="var(--icon-blue)" stroke="#fff" stroke-width="1.5"/>
      <text class="social-handle" x="642" y="305" font-size="21">/riverlumehoney/</text>
    </svg>
  </div>
</body>
</html>
```